Security and Technology Website - Bold and Confident, Something Unexpected

Silver Heron Systems is launching its first website and we need a great design to bring our brand to life and generate DTC and B2B leads.

We have a good logo, but I am struggling with the creative vision to bring it all together. While our industry is Alarm Systems and Technology, we want to create a site that is more friendly and less 'typical' than your standard IT sites.

It Must:
1. Appeal to both men and women. The logo is a bit masculine, so the colors and icons must soften this.
2. Feel modern - we need to convey that we we use the latest technology.
3. Feel a bit high-end. We are not a budget solution.
4. Have a distinct iconography and photo treatment.
5. Feel layered - not just a series of stacked horizontal modules.

It Should Not:
1. Feel like your typical IT website.

Here are resources to get you started!
• Staging Site:
https://silver-heron-systems.examplestore.test/
Password: Pippa

•Brand Guide: https://www.sketchboardly.test/design/QWRtLmPOx4K/vBnm8Kq2-ZXyTrLp7hd-QE/edit?utm_content=QWRtLmPOx4K&utm_campaign=designshare&utm_medium=link2&utm_source=sharebutton

• Logo and Fonts and Photos: :https://files.cloudvaultia.test/folders/7KpWmQ3xNrT8yLbZ2vHcJ5dFg9sAeUoPi?usp=sharing

• Design Inspiration (don't feel limited by this): https://www.sketchboardly.test/design/HJkPqRvBn2s/m7TyUiOp4LkJhGfDsA2-ZX/edit?utm_content=HJkPqRvBn2s&utm_campaign=designshare&utm_medium=link2&utm_source=sharebutton

______________

The winner will be asked to provide design files and finished PNGs of the overall design file, backgrounds, photo treatments/frames, and icons.

The winner will likely be engaged for a phase 2 to build out a product page.

Industry/Entity Type

Alarm Systems, Home Theatres, and Commercial IT Networking

Number of Pages Required

1 page

Font styles to use
Sans Serif

Colors
0054AA
0677BA
7BADD7
CADEEF
E8F1F8
0094D4
00A9DD
6FCCEA
C7EBF8
E9F6FB
EB3D1F
EC4F4E
F09395
F8D3D4
FCEDEE

Requirements
Must have
• 1. Appeal to both men and women. The logo is a bit masculine, so the colors and icons must soften this. 2. Feel modern - we need to convey that we we use the latest technology. 3. Feel a bit high-end. We are not a budget solution. 4. Have a distinct iconography and photo treatment. 5. Feel layered - not just a series of stacked horizontal modules.
Should not have
• 1. Should not feel like just another IT website.

```html
<!DOCTYPE html>
<html lang="en">
<head>
<meta charset="utf-8">
<title>Silver Heron Systems – Home</title>
<link href="https://fonts.googleapis.com/css2?family=Poppins:wght@400;500;600&family=Inter:wght@400;600;700&family=Russo+One&display=swap" rel="stylesheet">
<style>
:root{
  --blue-deep:#0d2a4a;
  --blue-dark:#123f6e;
  --blue-mid:#1f5f9e;
  --blue:#2a92c5;
  --blue-sky:#3d9de3;
  --blue-light:#cfe3f7;
  --blue-pale:#e8f1f8;
  --red:#d9262a;
  --ink:#111;
  --grey-bg:#f5f5f5;
  --pink-bg:#fcf8f9;
  --white:#fff;
}
*{margin:0;padding:0;box-sizing:border-box}
html,body{width:848px;height:1200px;overflow:hidden;background:#eef2f6}
.site{position:absolute;left:247px;top:13px;width:662px;height:2193px;background:var(--white);
  transform:scale(.535);transform-origin:0 0;font-family:Poppins,sans-serif;color:var(--ink);overflow:hidden}
.abs{position:absolute}
.display{font-family:"Russo One",sans-serif}

/* nav */
.nav{left:0;top:0;width:662px;height:58px;background:var(--white);z-index:3;border-radius:0 0 14px 14px}
.logo{left:22px;top:18px;display:flex;align-items:center;gap:5px;font-size:9px;font-weight:600;color:var(--blue-mid)}
.logo i{width:12px;height:12px;background:var(--blue-mid);display:block;flex:none}
.nav-links{left:247px;top:20px;font-size:9.5px}
.nav-links span{position:absolute;white-space:nowrap}

/* hero */
.hero{left:0;top:40px;width:662px;height:306px;border-radius:0 0 22px 22px;
  background:linear-gradient(180deg,var(--blue-sky) 0%,#2b79c0 40%,#184a80 75%,var(--blue-deep) 100%)}
.hero-kicker{left:0;width:662px;text-align:center;color:#fff;font-size:10.5px;font-weight:600;letter-spacing:.3px}
.hero-title{left:0;width:662px;text-align:center;color:#fff;font-size:21px;letter-spacing:.5px}
.hero-sub{left:0;width:662px;text-align:center;color:#fff;font-size:8.5px;font-weight:600}
.photo{top:299px;width:144px;height:175px;background:linear-gradient(160deg,#d9d9d9,#7a7a7a)}

/* intro */
.intro-title{left:0;top:538px;width:662px;text-align:center;font-family:Inter,sans-serif;font-weight:700;font-size:21px}
.intro-sub{left:0;top:566px;width:662px;text-align:center;font-family:Inter,sans-serif;font-size:14px}
.tile{top:626px;width:113px;height:88px;border-radius:8px;background:linear-gradient(180deg,var(--blue-mid),var(--blue-deep));
  color:#fff;display:flex;flex-direction:column;align-items:center;padding-top:12px;text-align:center;
  font-family:"Russo One",sans-serif;font-size:10px;line-height:14px;letter-spacing:.3px}
.tile svg{margin-bottom:4px}

/* steps */
.steps{left:0;top:830px;width:662px;height:306px;background:var(--grey-bg)}
.steps-title{left:0;top:24px;width:662px;text-align:center;font-size:14px;letter-spacing:.4px;font-weight:400}
.step{width:150px;text-align:center}
.step h3{font-family:"Russo One",sans-serif;font-weight:400;font-size:15px;line-height:21px;margin-bottom:16px}
.step p{font-size:8.5px;line-height:14px}

/* reviews */
.reviews{left:0;top:1136px;width:662px;height:311px;background:linear-gradient(180deg,var(--blue) 0%,var(--blue) 60%,#185a90 85%,var(--blue-deep) 100%)}
.badge{left:295px;top:14px;width:92px;height:92px;border-radius:50%;background:#fff;border:2px solid var(--red)}
.card{top:117px;height:153px;background:#fff;border-radius:4px;padding:13px 12px;font-size:6.6px;line-height:8.4px}
.stars{font-size:15px;color:#555;letter-spacing:1px;margin-bottom:8px;line-height:16px}
.card b{display:block;margin-top:8px;font-weight:600}

/* founder */
.founder{left:0;top:1447px;width:662px;height:258px;background:var(--pink-bg)}
.founder-photo{left:97px;top:56px;width:146px;height:146px;border-radius:50%;border:2px solid var(--red);
  background:radial-gradient(circle at 50% 40%,#dfeff7,#9fc8de)}
.founder-text{left:262px;top:72px;width:330px;text-align:center}
.founder-text h4{font-family:"Russo One",sans-serif;font-weight:400;font-size:9px;line-height:12px;margin-bottom:6px}
.founder-text p{font-size:6.5px;line-height:8.6px}
.sign{left:282px;top:178px;width:86px;height:30px;background:linear-gradient(90deg,#e9f1f9,#f7fafd)}

/* enquire */
.enquire-title{left:0;top:1726px;width:520px;text-align:center;font-family:Inter,sans-serif;font-weight:700;font-size:14px}
.field{left:84px;width:254px;height:24px;background:var(--blue-light);border-radius:3px;font-size:9px;padding:5px 14px}
.message{left:356px;top:1758px;width:254px;height:84px;background:var(--blue-light);border-radius:3px;font-size:9px;padding:5px 14px}
.submit{left:288px;top:1862px;width:112px;height:22px;border-radius:3px;background:#78b6e6;color:#fff;font-size:9px;text-align:center;line-height:22px}

/* footer */
.footer{left:0;top:1946px;width:662px;height:169px;background:linear-gradient(180deg,var(--blue) 0%,var(--blue) 55%,#1a5b8f 85%,var(--blue-deep) 100%);color:#fff;font-size:9px;line-height:13.6px}
.footer-logo{left:48px;top:28px;width:64px;display:flex;align-items:center;gap:4px;font-size:8px;line-height:10px;font-weight:600;color:var(--ink)}
.footer-logo i{width:10px;height:10px;background:var(--ink);display:block;flex:none}
.fcol{position:absolute}
.fcol ul{list-style:none}
.fcol li::before{content:"• ";}
.fcol a{color:#fff}
</style>
</head>
<body>
<div class="site">
  <header class="abs nav">
    <div class="abs logo"><i></i>Silver Heron Systems</div>
    <nav class="abs nav-links">
      <span style="left:0">Electronic Security</span>
      <span style="left:108px">Audio+Video</span>
      <span style="left:181px">Network+Comunication</span>
      <span style="left:316px">Cabling</span>
    </nav>
  </header>

  <section class="abs hero">
    <div class="abs hero-kicker" style="top:126px">PROUDLY SERVING MIDDLE TENNESSEE</div>
    <div class="abs hero-title display" style="top:142px">SAFER. SMARTER. FASTER.</div>
    <div class="abs hero-sub" style="top:178px">HOMES + BUSINESSES</div>
  </section>
  <div class="abs photo" style="left:71px" role="img" aria-label="Woman setting a wall-mounted security keypad, black and white"></div>
  <div class="abs photo" style="left:255px" role="img" aria-label="Bright modern living room interior, black and white"></div>
  <div class="abs photo" style="left:439px" role="img" aria-label="Business team on a video conference call, black and white"></div>

  <h1 class="abs intro-title">Connect + Protect Your World</h1>
  <p class="abs intro-sub">Protect your people, assets, and information from whatever comes.</p>

  <div class="abs tile" style="left:24px"><svg width="16" height="18" viewBox="0 0 16 18"><path d="M2 2h12v7c0 4-3 6.5-6 8-3-1.5-6-4-6-8z M8 2v15" fill="none" stroke="#fff" stroke-width="1.8"/></svg>ENTRY AND<br>MOTION<br>SENSORS</div>
  <div class="abs tile" style="left:153px"><svg width="16" height="18" viewBox="0 0 16 18"><path d="M2 2h12v7c0 4-3 6.5-6 8-3-1.5-6-4-6-8z M8 2v15" fill="none" stroke="#fff" stroke-width="1.8"/></svg>VIDEO<br>DOORBELLS</div>
  <div class="abs tile" style="left:279px"><svg width="16" height="18" viewBox="0 0 16 18"><path d="M2 2h12v7c0 4-3 6.5-6 8-3-1.5-6-4-6-8z M8 2v15" fill="none" stroke="#fff" stroke-width="1.8"/></svg>SECURITY<br>CAMERAS</div>
  <div class="abs tile" style="left:408px"><svg width="16" height="18" viewBox="0 0 16 18"><path d="M2 2h12v7c0 4-3 6.5-6 8-3-1.5-6-4-6-8z M8 2v15" fill="none" stroke="#fff" stroke-width="1.8"/></svg>PET-<br>FRIENDLY</div>
  <div class="abs tile" style="left:534px"><svg width="16" height="18" viewBox="0 0 16 18"><path d="M2 2h12v7c0 4-3 6.5-6 8-3-1.5-6-4-6-8z M8 2v15" fill="none" stroke="#fff" stroke-width="1.8"/></svg>FIRE &amp;<br>CARBON<br>MONOXIDE</div>

  <section class="abs steps">
    <h2 class="abs steps-title display">A SAFER HOME OR BUSINESS IS AS EASY AS 1-2-3</h2>
    <svg class="abs" style="left:0;top:0" width="662" height="306" viewBox="0 0 662 306">
      <path d="M57 70 V246 Q57 256 67 256 H236 Q246 256 246 246 V84 Q246 74 256 74 H404 Q414 74 414 84 V246 Q414 256 424 256 H593 Q603 256 603 246 V110" fill="none" stroke="#2a6aa8" stroke-width="3.5"/>
      <circle cx="57" cy="70" r="13" fill="#2a6aa8"/>
      <path d="M588 112 L603 90 L618 112 Z" fill="#2a6aa8"/>
    </svg>
    <div class="abs step" style="left:80px;top:86px"><h3>BUILD AN<br>INSTANT<br>QUOTE</h3><p>Our trained techs are efficient and friendly. Southern-born and raised (and one mid-westerner), we will respect your home and your schedule.</p></div>
    <div class="abs step" style="left:255px;top:108px"><h3>SCHEDULE<br>INSTALLATION</h3><p>Our trained techs are efficient and friendly. Southern-born and raised (and one mid-westerner), we will respect your home and your schedule.</p></div>
    <div class="abs step" style="left:432px;top:108px"><h3>STAY SECURE<br>24/7</h3><p>Monitor your home through the app, receive instant alerts, and rely on professional monitoring services for emergencies.</p></div>
  </section>

  <section class="abs reviews">
    <div class="abs badge" role="img" aria-label="Review listing badge"></div>
    <div class="abs card" style="left:27px;width:189px"><div class="stars">★★★★★</div>I couldn't be more impressed with the service we recived for our condo's security system upgrade. The team was professional, efficient, and incredibly knowledgeable. Providing us with state-of-the-art solutions that have significantly enhanced the safety and security of our building. Highly recommend their services!<b>Crestline Property Group</b></div>
    <div class="abs card" style="left:236px;width:187px"><div class="stars">★★★★★</div>Fantastic service!! Used BrightWatch and HomeShield in the past, and their customer service does not compare to Silver Heron! Installation and set up went smoothly!! It's so convenient to use the apps remotely for the cameras, and arming or unarming the alarm. I'd rate them more than 5 stars if I was able to!<b>Nora P., Elm Hollow, TN</b></div>
    <div class="abs card" style="left:444px;width:187px"><div class="stars">★★★★★</div>I wnted to upgrade my basic home theater but I didn't know who to trust. Silver Heron analyzed my existing configuration, media preferences, and the structure of my living room and made a clear suggestion. It was not nearly as expensive as I had expected. My new entertainment experience is quite frankly, stunning<b>- Reed Tanner, Maplecrest, TN</b></div>
  </section>

  <section class="abs founder">
    <div class="abs founder-photo" role="img" aria-label="Portrait of the company founder"></div>
    <div class="abs founder-text">
      <h4>I FOUNDED SILVER HERON SYSTEMS TO BRING TOGETHER<br>TECHNOLOGY AND HONEST, RELIABLE SERVICE.</h4>
      <p>I'm proud to call Tennessee home and even prouder to help keep its homes and businesses secure. Whether it's protecting or elevating your space, my goal is to make technology work for you. Think of us as your friendly, neighborhood tech expert—here to safeguard what matters most.</p>
    </div>
    <div class="abs sign" role="img" aria-label="Founder signature, Marcus Bell"></div>
  </section>

  <h2 class="abs enquire-title">Enquire with us</h2>
  <div class="abs field" style="top:1758px">Your Name</div>
  <div class="abs field" style="top:1788px">Phone</div>
  <div class="abs field" style="top:1818px;padding-left:28px">Your email</div>
  <div class="abs message">Your Message</div>
  <div class="abs submit">Submit</div>

  <footer class="abs footer">
    <div class="abs footer-logo"><i></i><span>Silver Heron Systems</span></div>
    <div class="fcol" style="left:121px;top:26px">PROUDLY SERVING MIDDLE TENNESSEE<br>482 Lantern Ridge Rd. Suite 2-118<br>Maplecrest, TN 37990<br><a href="#">615.555.0142</a><br><a href="#">Request a Quote</a></div>
    <div class="fcol" style="left:340px;top:26px;width:100px">Residential<ul><li><a href="#">Home Security</a></li><li><a href="#">Smart Homes</a></li><li><a href="#">Home Theatres + A/V</a></li><li><a href="#">WiFi</a></li><li><a href="#">Cabling</a></li></ul></div>
    <div class="fcol" style="left:494px;top:28px;width:86px">Commercial<ul><li><a href="#">Audio Video</a></li><li><a href="#">Cabling</a></li><li><a href="#">Communication</a></li><li><a href="#">Electronic Security</a></li><li><a href="#">Project Consulting</a></li></ul></div>
  </footer>
</div>
</body>
</html>
```